Non fiction leadership Book Cover design needed for “Hold Fast: Forge A Steady Track”

I need a front cover design for a new book 6 X 9 traditional non-fiction book.

Title: "Hold FAST - Forge A Steady Track"

The subtitle is not finalized- so use 2 lines of smaller dummy text

My brand guide is attached (please use the tan color sparingly)

I'd like to see FAST look like it is in motion and "flying" across the page

Need CREATIVE designs and options

Do not want my picture on the front cover - I do want it on the back cover.

On the front cover I’d like to see creative use of font to create movement on “FAST”

Target Market(s)

Business leaders

Industry/Entity Type

Aviation

Font styles to use
Other font styles liked:
• See style guide- can add additional font (modern script or san serif)

Colors
0054AA
0677BA
7BADD7
CADEEF
E8F1F8
EB3D1F
EC4F4E
F09395
F8D3D4
FCEDEE

Requirements
Must have
• Creative font use, using perspective to create movement/motion on FAST
Should not have
• My picture on the front cover- my picture should be on the back cover

```html
<!DOCTYPE html>
<html lang="en">
<head>
<meta charset="utf-8">
<title>Hold Fast: Forge A Steady Track — Front Cover</title>
<link rel="stylesheet" href="https://fonts.googleapis.com/css2?family=Sacramento&family=Playfair+Display:wght@900&family=Montserrat:wght@500&display=swap">
<style>
  :root {
    --backdrop: #dcdcd8;
    --cover-edge: #080818;
    --cover-ink: #070707;
    --tan: #c4864a;
    --tan-soft: rgba(196, 134, 74, 0.55);
    --shadow: #2e2e2e;
  }
  * { margin: 0; padding: 0; box-sizing: border-box; }
  html, body {
    width: 1200px;
    height: 864px;
    overflow: hidden;
    background: var(--backdrop);
  }
  .cover {
    position: absolute;
    left: 330px;
    top: 27px;
    width: 540px;
    height: 810px;
    background: var(--cover-edge);
    padding: 14px;
  }
  .cover-face {
    position: relative;
    width: 100%;
    height: 100%;
    background: var(--cover-ink);
    overflow: hidden;
  }
  .wing {
    position: absolute;
    z-index: 0;
    border-radius: 50%;
    background: radial-gradient(ellipse at center, var(--tan-soft) 0%, rgba(196, 134, 74, 0.18) 55%, rgba(196, 134, 74, 0) 72%);
  }
  .wing-left {
    left: 6px;
    top: 400px;
    width: 170px;
    height: 110px;
    transform: rotate(18deg);
  }
  .wing-right {
    left: 372px;
    top: 210px;
    width: 130px;
    height: 180px;
    transform: rotate(24deg);
  }
  .book-title {
    position: relative;
    z-index: 1;
    font-weight: normal;
  }
  .title-script {
    position: absolute;
    top: 70px;
    left: 0;
    width: 100%;
    text-align: center;
    padding-right: 30px;
    font-family: "Sacramento", cursive;
    font-size: 180px;
    line-height: 1;
    color: var(--tan);
  }
  .title-main {
    position: absolute;
    top: 330px;
    left: 0;
    width: 100%;
    height: 150px;
    display: flex;
    justify-content: center;
    align-items: flex-end;
    font-family: "Playfair Display", serif;
    font-weight: 900;
    font-size: 118px;
    line-height: 1;
    color: var(--tan);
    text-shadow: -6px 6px 0 var(--shadow);
  }
  .title-main .letter { display: inline-block; }
  .title-main .step-1 { transform: translateY(0); }
  .title-main .step-2 { transform: translateY(-24px); }
  .title-main .step-3 { transform: translateY(-48px); }
  .title-main .step-4 { transform: translateY(-72px); }
  .subtitle {
    position: absolute;
    z-index: 1;
    top: 530px;
    left: 0;
    width: 100%;
    text-align: center;
    font-family: "Montserrat", sans-serif;
    font-weight: 500;
    font-size: 21px;
    line-height: 1.9;
    letter-spacing: 9px;
    color: var(--tan);
  }
  .author {
    position: absolute;
    z-index: 1;
    top: 690px;
    left: 0;
    width: 100%;
    text-align: center;
    font-family: "Montserrat", sans-serif;
    font-weight: 500;
    font-size: 21px;
    letter-spacing: 10px;
    color: var(--tan);
  }
</style>
</head>
<body>
  <main class="cover">
    <div class="cover-face">
      <div class="wing wing-left" role="img" aria-label="Tan feathered wing sweeping out to the left"></div>
      <div class="wing wing-right" role="img" aria-label="Tan feathered wing rising to the upper right"></div>
      <h1 class="book-title">
        <span class="title-script">Hold</span>
        <span class="title-main" aria-label="FAST">
          <span class="letter step-1">F</span><span class="letter step-2">A</span><span class="letter step-3">S</span><span class="letter step-4">T</span>
        </span>
      </h1>
      <p class="subtitle">“FORGE A<br>STEADY TRACK”</p>
      <p class="author">AUTHOR NAME</p>
    </div>
  </main>
</body>
</html>
```